For our product portfolio we need a new packaging design. Our product is a Guaraná-derived energy in powder form. It is sold in small bags, between 350 x 400 mm and 700 x 800 mm, and also in boxes e.g. in the size of 240 x 160 x 45mm.

Our goal is to get creative product design which can be used for
a) the small bags,
b) the boxes, and
c) our Web site logo.

Target Market(s)

Our current target market are computer and Internet geeks. Therefore, we used a LOL-cat in our current/previous design. With the new design we would like to address a broader audience. It would be nice to see logos and packaging designs that are suitable to catch the attention of both geeks as well as normal folks.

Our target audience are people who would buy energy drinks or drink a lot of coffee.

The target audience are young people who work hard and/or go to parties and festivals. The design should be rather playful and funny than serious business.

Industry/Entity Type

Product

Requirements
Must have
• 1. A relationship to the nature product Guaraná. You could, for example, use the red fruits and green leaves of the guarana plant in the design to signal that the product is organic and good for your health. Take a look at http://en.plinthopedia.example/wiki/Guarana for inspirations.
• 2. Our product name is "Velora Fizzpulver"
• 3. The small bags must have certain information in multiple languages (please see image attached as file 1 for reference). We will tell you the specifics when your design is selected as one of our favorites. However, please keep some space in your packaging design for the information text.
• 4. The boxes must have certain information in multiple languages (please see image attached as file 3 for reference). We will tell you the specifics when your design is selected as one of our favorites.
• 5. The graphics must be delivered in an open format so that we can make changes and adjustments after the competition has finished.
• 6. The graphics for packaging must use CMYK colors with at least 600dpi. The logo must use RGB colors with 72dpi.
• Please avoid resemblance with other trademarks, such as Tovimba Borealis.
Nice to have
• A brand identity that is appealing to the "Internet community", e.g. a LOL-cat animal, an Internet meme, or the like.
• Another idea would be to use a hybrid animal, such as http://www.snipmorphs.example/gallery/data/418/medium/stretch_snipmorphs.jpg
• In any case, creative and imaginative submissions are preferred over boring submissions. We are open to all ideas.

```html
<!DOCTYPE html>
<html lang="en">
<head>
<meta charset="utf-8">
<title>Velora Fizzpulver – Cherry pouch</title>
<link href="https://fonts.googleapis.com/css2?family=Ubuntu:wght@500&family=Roboto+Condensed:wght@400;700&display=swap" rel="stylesheet">
<style>
  :root {
    --stage: #ececec;
    --pouch-black: #111111;
    --brand-red: #e3191c;
    --white: #ffffff;
    --edge-grey: #8a8a8a;
    --leaf-green: #4f9a3a;
    --owl-grey: #d9d9d9;
    --seal-grey: #e6e6e6;
  }
  * { margin: 0; padding: 0; box-sizing: border-box; }
  html, body { width: 1200px; height: 870px; overflow: hidden; }
  body {
    background: radial-gradient(ellipse at center, #f7f7f7 0%, var(--stage) 70%, #dcdcdc 100%);
    font-family: "Roboto Condensed", Arial, sans-serif;
    position: relative;
  }
  .pouch {
    position: absolute;
    top: 120px;
    width: 390px;
    height: 630px;
    background: var(--pouch-black);
    overflow: hidden;
    box-shadow: 0 18px 40px rgba(0,0,0,.25);
  }
  .pouch--front { left: 170px; }
  .pouch--back { left: 640px; }
  .pouch__art { position: absolute; inset: 0; }

  .brand-name {
    position: absolute;
    font-family: "Ubuntu", Arial, sans-serif;
    font-weight: 500;
    color: var(--white);
    text-transform: uppercase;
    white-space: nowrap;
    letter-spacing: .5px;
  }
  .mascot {
    position: absolute;
    background: radial-gradient(ellipse at 50% 40%, var(--white) 0%, var(--owl-grey) 75%);
    border-radius: 44% 44% 40% 40%;
  }
  .guarana-sprig {
    position: absolute;
    background: radial-gradient(circle at 60% 60%, #c4261f 0%, #8e1a14 45%, var(--leaf-green) 80%, transparent 82%);
    border-radius: 50%;
  }

  /* front */
  .pouch--front .mascot { left: 140px; top: 345px; width: 120px; height: 150px; }
  .pouch--front .guarana-sprig { left: 45px; top: 440px; width: 75px; height: 75px; }
  .pouch--front .brand-name { left: 52px; top: 548px; font-size: 30px; }
  .flavour {
    position: absolute;
    left: 318px; top: 375px;
    transform: translate(-50%, -50%) rotate(-90deg);
    color: var(--brand-red);
    font-family: "Ubuntu", Arial, sans-serif;
    font-weight: 500;
    font-size: 29px;
    letter-spacing: 11px;
  }

  /* back */
  .pouch--back .mascot { left: 160px; top: 38px; width: 70px; height: 88px; }
  .pouch--back .guarana-sprig { left: 95px; top: 88px; width: 50px; height: 50px; }
  .pouch--back .brand-name { left: 85px; top: 140px; font-size: 22px; color: var(--brand-red); }

  .info-panel {
    position: absolute;
    left: 38px; top: 178px;
    width: 312px; height: 225px;
    border: 1.5px solid var(--white);
    border-radius: 10px;
    padding: 8px 10px;
    color: var(--white);
  }
  .info-panel__intro { font-size: 7.5px; line-height: 1.25; text-align: justify; }
  .languages { display: flex; gap: 6px; margin-top: 14px; }
  .language {
    flex: 1;
    position: relative;
    border: 1px solid var(--white);
    border-radius: 7px;
    padding: 10px 5px 5px;
    font-size: 6.6px;
    line-height: 1.25;
    text-align: justify;
    height: 120px;
  }
  .language__tag {
    position: absolute;
    top: -8px; left: 8px;
    background: var(--white);
    color: var(--brand-red);
    border: 1.5px solid var(--brand-red);
    border-radius: 50%;
    font-weight: 700;
    font-size: 8px;
    padding: 1px 5px;
  }

  .nutrition {
    position: absolute;
    left: 38px; top: 418px;
    width: 212px;
    background: var(--brand-red);
    color: var(--white);
    font-size: 8px;
    padding: 3px 4px 5px;
  }
  .nutrition__title { text-align: center; font-weight: 700; font-size: 8.5px; margin-bottom: 3px; }
  .nutrition table { width: 100%; border-collapse: collapse; }
  .nutrition td { border: 1px solid rgba(255,255,255,.55); padding: 1px 2px; vertical-align: top; font-weight: 700; }
  .nutrition td small { display: block; font-weight: 400; font-size: 6.5px; }
  .nutrition .value { text-align: right; }
  .caution {
    position: absolute;
    left: 254px; top: 418px;
    width: 96px;
    background: var(--brand-red);
    color: var(--white);
    font-size: 7px;
    line-height: 1.3;
    padding: 3px 4px;
  }
  .caution strong { display: block; font-size: 8.5px; }

  .dosage {
    position: absolute;
    left: 160px; top: 520px;
    display: flex; align-items: center; gap: 5px;
    color: var(--brand-red);
    font-weight: 700; font-size: 17px;
  }
  .dosage__one { background: var(--brand-red); color: var(--pouch-black); padding: 0 5px; }
  .net-weight {
    position: absolute;
    left: 160px; top: 552px;
    color: var(--white);
    font-family: "Ubuntu", Arial, sans-serif;
    font-size: 30px;
  }
  .certification-badge {
    position: absolute;
    left: 262px; top: 510px;
    width: 78px; height: 78px;
    border-radius: 50%;
    background: var(--seal-grey);
  }
</style>
</head>
<body>

<section class="pouch pouch--front" aria-label="Front of the cherry pouch">
  <svg class="pouch__art" viewBox="0 0 390 630" aria-hidden="true">
    <polygon points="0,0 340,0 0,228" fill="var(--brand-red)"/>
    <g stroke="var(--white)" stroke-width="9">
      <line x1="0" y1="245" x2="400" y2="-23"/>
      <line x1="0" y1="264" x2="420" y2="-18"/>
      <line x1="0" y1="283" x2="440" y2="-12"/>
      <line x1="0" y1="302" x2="460" y2="-6"/>
    </g>
    <g stroke-width="2">
      <line x1="372" y1="0" x2="372" y2="630" stroke="var(--edge-grey)"/>
      <line x1="376" y1="0" x2="376" y2="630" stroke="var(--white)"/>
      <line x1="380" y1="0" x2="380" y2="630" stroke="var(--edge-grey)"/>
      <line x1="384" y1="0" x2="384" y2="630" stroke="var(--white)"/>
      <line x1="388" y1="0" x2="388" y2="630" stroke="var(--edge-grey)"/>
      <line x1="4" y1="0" x2="4" y2="630" stroke="var(--edge-grey)"/>
    </g>
  </svg>
  <div class="flavour">CHERRY</div>
  <div class="mascot" role="img" aria-label="Owl mascot illustration"></div>
  <div class="guarana-sprig" role="img" aria-label="Guarana fruits with green leaves illustration"></div>
  <div class="brand-name">Velora Fizzpulver</div>
</section>

<section class="pouch pouch--back" aria-label="Back of the cherry pouch">
  <svg class="pouch__art" viewBox="0 0 390 630" aria-hidden="true">
    <polygon points="170,0 390,0 390,135" fill="var(--brand-red)"/>
    <polygon points="0,440 0,630 150,630" fill="var(--brand-red)"/>
    <g stroke-width="2">
      <line x1="4" y1="0" x2="4" y2="630" stroke="var(--edge-grey)"/>
      <line x1="8" y1="0" x2="8" y2="630" stroke="var(--white)"/>
      <line x1="372" y1="0" x2="372" y2="630" stroke="var(--edge-grey)"/>
      <line x1="376" y1="0" x2="376" y2="630" stroke="var(--white)"/>
      <line x1="380" y1="0" x2="380" y2="630" stroke="var(--edge-grey)"/>
      <line x1="384" y1="0" x2="384" y2="630" stroke="var(--white)"/>
    </g>
  </svg>
  <div class="mascot" role="img" aria-label="Owl mascot illustration"></div>
  <div class="guarana-sprig" role="img" aria-label="Guarana fruits with green leaves illustration"></div>
  <div class="brand-name">Velora Fizzpulver</div>

  <div class="info-panel">
    <p class="info-panel__intro">Lorem ipsum dolor sit amet, consectetuer adipiscing elit, sed diam nonummy nibh euismod tincidunt ut laoreet dolore magna aliquam erat volutpat. Ut wisi enim ad minim veniam, quis nostrud exerci tation ullamcorper suscipit lobortis nisl ut aliquip ex ea commodo consequat. Duis autem vel eum iriure dolor in hendrerit in vulputate velit esse molestie consequat, vel illum dolore eu feugiat nulla facilisis at vero eros et accumsan et iusto odio dignissim qui blandit praesent luptatum zzril</p>
    <div class="languages">
      <div class="language"><span class="language__tag">ENG</span>Lorem ipsum dolor sit amet, consectetuer adipiscing elit, sed diam nonummy nibh euismod tincidunt ut laoreet dolore magna aliquam erat volutpat. Ut wisi enim ad minim veniam, quis nostrud exerci tation ullamcorper suscipit lobortis nisl ut aliquip ex ea commodo consequat. Duis autem</div>
      <div class="language"><span class="language__tag">FR</span>Lorem ipsum dolor sit amet, consectetuer adipiscing elit, sed diam nonummy nibh euismod tincidunt ut laoreet dolore magna aliquam erat volutpat. Ut wisi enim ad minim veniam, quis nostrud exerci tation ullamcorper suscipit lobortis nisl ut aliquip ex ea commodo consequat. Duis autem</div>
      <div class="language"><span class="language__tag">ESP</span>Lorem ipsum dolor sit amet, consectetuer adipiscing elit, sed diam nonummy nibh euismod tincidunt ut laoreet dolore magna aliquam erat volutpat. Ut wisi enim ad minim veniam, quis nostrud exerci tation ullamcorper suscipit lobortis nisl ut aliquip ex ea commodo consequat. Duis autem</div>
    </div>
  </div>

  <div class="nutrition">
    <div class="nutrition__title">Nutritional Information per 100ml serving</div>
    <table>
      <tr><td>Energy</td><td class="value">188kJ<br>45 kcal</td><td>Carbohydrate<small>Sugar</small></td><td class="value">10.4g</td><td>Fiber</td><td class="value">0.1 g</td></tr>
      <tr><td>Protein</td><td class="value">0.4 g</td><td>Fat<small>Saturated Fats</small></td><td class="value">0.1 g</td><td>Sodium</td><td class="value">0.1 mg</td></tr>
    </table>
  </div>
  <div class="caution"><strong>Enthält Guaraná.</strong>Erhöhter Koffeingehalt. Für Kinder, Schwangere und koffein-empfindliche Personen nicht empfohlen.</div>

  <div class="dosage">
    <span class="dosage__one">1</span><span>=</span>
    <svg width="40" height="24" viewBox="0 0 40 24" aria-label="cup icon, one and a half cups">
      <path d="M4 4 H30 V14 Q30 20 24 20 H10 Q4 20 4 14 Z" fill="none" stroke="var(--brand-red)" stroke-width="2"/>
      <path d="M30 7 Q37 7 37 11 Q37 15 30 15" fill="none" stroke="var(--brand-red)" stroke-width="2"/>
      <line x1="0" y1="23" x2="34" y2="23" stroke="var(--brand-red)" stroke-width="2"/>
      <text x="17" y="16" font-size="11" font-weight="700" text-anchor="middle" fill="var(--brand-red)" font-family="Roboto Condensed, sans-serif">1½</text>
    </svg>
  </div>
  <div class="net-weight">℮ 20g</div>
  <div class="certification-badge" role="img" aria-label="Organic certification badge"></div>
</section>

</body>
</html>
```